Business Card Design

I am a classical pilates instructor. I have a home studio, teach out a of a large studio downtown, and teach at on location corporate settings
I like my card to be very simple and clean.
I would like a silhouette of the picture I'm uploading on my design. In the upload section it looks like the picture is cut off and only showing a leg in the air...let me know if you can open up the entire picture.

Industry/Entity Type
Business
Contact Information for Business Card
Moira Kestley Pilates
Certified - The Pilates Center of Harnley
mo.kestley58@postvale.net
615.473.2186

```html
<!DOCTYPE html>
<html lang="en">
<head>
<meta charset="utf-8">
<title>Moira Kestley Pilates – Business Card</title>
<link rel="stylesheet" href="https://fonts.googleapis.com/css2?family=Poiret+One&family=Open+Sans:wght@400;600&display=swap">
<style>
  :root {
    --backdrop: #1c1c1c;
    --card-light-1: #f4f4f4;
    --card-light-2: #bdbdbd;
    --card-dark-1: #2a2a2a;
    --card-dark-2: #050505;
    --ink: #161616;
    --ink-soft: #3a3a3a;
    --accent: #e8731a;
    --ring: #8a7a70;
    --name-grey: #9a9a9a;
    --silhouette: #111111;
  }
  * { margin: 0; padding: 0; box-sizing: border-box; }
  html, body { width: 1200px; height: 1134px; overflow: hidden; }
  body {
    background: var(--backdrop);
    font-family: "Open Sans", sans-serif;
    position: relative;
  }
  .card {
    position: absolute;
    width: 540px;
    height: 309px;
    border-radius: 4px;
    overflow: hidden;
    box-shadow: 0 10px 30px rgba(0,0,0,.6);
  }
  .card--front {
    left: 40px; top: 300px;
    background: radial-gradient(ellipse at 60% 35%, var(--card-light-1), var(--card-light-2));
  }
  .card--back {
    left: 620px; top: 300px;
    background: radial-gradient(ellipse at 50% 40%, var(--card-dark-1), var(--card-dark-2));
  }
  .front-divider { position: absolute; inset: 0; }
  .silhouette-area {
    position: absolute;
    left: 18px; top: 20px;
    width: 210px; height: 270px;
    border-radius: 40% 60% 30% 50%;
    background: radial-gradient(ellipse at 50% 50%, #2a2a2a, var(--silhouette) 70%, rgba(17,17,17,0) 72%);
  }
  .brand-circle {
    border-radius: 50%;
    background: radial-gradient(circle at 50% 40%, #3a3a3a, #0a0a0a);
    border: 6px solid var(--ring);
    display: flex; align-items: center; justify-content: center;
    text-align: center;
  }
  .brand-name {
    font-family: "Poiret One", sans-serif;
    color: var(--accent);
    line-height: 1.1;
  }
  .card--front .brand-circle {
    position: absolute; left: 316px; top: 22px;
    width: 96px; height: 96px;
  }
  .card--front .brand-name { font-size: 15px; }
  .contact {
    position: absolute; left: 268px; top: 134px;
    color: var(--ink);
  }
  .contact__name {
    font-family: "Poiret One", sans-serif;
    font-size: 32px; letter-spacing: 1px;
  }
  .contact__title {
    font-family: "Poiret One", sans-serif;
    font-size: 24px; margin-top: -2px;
  }
  .contact__studio { font-size: 12px; color: var(--ink-soft); margin-bottom: 14px; }
  .contact__line {
    display: flex; align-items: center; gap: 8px;
    font-size: 12px; font-weight: 600; margin-top: 4px;
  }
  .contact__line svg { width: 14px; height: 14px; fill: var(--ink); }
  .card--back .brand-circle {
    position: absolute; left: 185px; top: 38px;
    width: 170px; height: 170px; border-width: 9px;
  }
  .card--back .brand-name { font-size: 24px; }
  .back-name {
    position: absolute; left: 0; right: 0; top: 232px;
    text-align: center;
    font-family: "Poiret One", sans-serif;
    font-size: 36px; letter-spacing: 3px;
    color: var(--name-grey);
  }
</style>
</head>
<body>
  <section class="card card--front" aria-label="Card front">
    <svg class="front-divider" viewBox="0 0 540 309" preserveAspectRatio="none" aria-hidden="true">
      <path d="M250 0 Q240 160 300 309" fill="none" stroke="#9c9c9c" stroke-width="1.5"/>
    </svg>
    <div class="silhouette-area" role="img" aria-label="Black silhouette of a woman in a pilates pose with legs raised"></div>
    <div class="brand-circle"><span class="brand-name">Moira<br>Kestley</span></div>
    <div class="contact">
      <div class="contact__name">Moira Kestley</div>
      <div class="contact__title">Pilates Certified</div>
      <div class="contact__studio">The Pilates Center of Harnley</div>
      <div class="contact__line">
        <svg viewBox="0 0 16 16" aria-hidden="true"><path d="M1 3h14v10H1z M2 4v.6l6 4.2 6-4.2V4z" fill-rule="evenodd"/></svg>
        mo.kestley58@postvale.net
      </div>
      <div class="contact__line">
        <svg viewBox="0 0 16 16" aria-hidden="true"><path d="M2 5c0-2 3-3 6-3s6 1 6 3v1h-3V5H5v1H2z M4 7h8l2 7H2z"/></svg>
        615.473.2186
      </div>
    </div>
  </section>

  <section class="card card--back" aria-label="Card back">
    <div class="brand-circle"><span class="brand-name">Moira<br>Kestley</span></div>
    <div class="back-name">Moira Kestley</div>
  </section>
</body>
</html>
```